Web Design Project for Web Agency

WHAT I NEED:
The design I need (PSD file) is for a microsite designed for employee recruitment for Brantley, a Web agency.
***Design for the 1st Page ONLY : "Manifeste"
OBJECTIVES OF THE WEBSITE:
1. To promote the agency's corporate culture and HR management principles.
2. To get people to apply on available jobs
ELEMENTS OF THE PAGE "MANIFESTE" :
1. Brantley logo (see attached files). Beside the logo must be the word "Carrières" ("Careers" in english)
***The logo is not final and there is NO branding for Brantley yet. That is why there are multiple files. So please feel free to be creative!
2. Main menu : 4 sections
Manifeste | Opportunités | Brantly | Postuler
3. Manifeste :
This page is the home page. It will present 2 main sections :
a. The agency's corporate culture :
- Title of the page is a question : "Do you embrace Brantley's corporate culture?"
- Then, presentation of the 5 corporate values, each with a title and short description
- At the end of the list of values, we want a button that says "Apply now"
b. The agency's HR management principles :
- Title of the page is a question : "Do you see yourself working at Brantley?"
- Then, presentation of the 5 Management principles, each with a title and short description
- At the end of the list of principles, we want a button that says "Apply now"
VISUAL INSPIRATION
To create each section of the "Manifeste" page, we want a design that will fit with the corporate culture:
- Brantley is BOLD
- Brantley is PROUD
- Brantley is PROFESSIONAL
- Brantley is ELEGANT
- Brantley is REFINED
We want something slick and modern. Here are some Website's that we like that can be of inspiration:
- http://www.studio-vetrak.com/en/services
- http://quorvinpanels.com/

```html
<!DOCTYPE html>
<html lang="en">
<head>
<meta charset="utf-8">
<title>Brantley Careers – Manifeste</title>
<link href="https://fonts.googleapis.com/css2?family=Bree+Serif&family=Lato:wght@300;400;700&family=Yanone+Kaffeesatz:wght@300;400;700&display=swap" rel="stylesheet">
<style>
  :root {
    --orange: #f47a3a;
    --orange-deep: #ee6a1e;
    --ink: #474747;
    --text: #4c4c4c;
    --rule: #e4e4e4;
    --footer: #62676a;
    --footer-text: #e2e4e5;
    --arrow-bg: rgba(108, 160, 186, 0.85);
  }
  * { box-sizing: border-box; margin: 0; padding: 0; }
  html, body { width: 1200px; height: 1021px; overflow: hidden; background: #fff; }
  body { position: relative; font-family: "Lato", sans-serif; color: var(--text); }

  .top-strip { position: absolute; left: 0; top: 0; width: 1200px; height: 11px; background: var(--orange); }

  .site-header { position: absolute; left: 0; top: 11px; width: 1200px; height: 79px; background: #fff; }
  .brand { position: absolute; left: 124px; top: 18px; width: 140px; }
  .brand-name { font-family: "Lato", sans-serif; font-weight: 700; font-size: 31px; line-height: 1; color: var(--orange); }
  .brand-tag { margin-top: 6px; font-size: 7.5px; letter-spacing: 2.6px; color: #555; font-weight: 400; }
  .brand-divider { position: absolute; left: 273px; top: 16px; width: 1px; height: 50px; background: #cfcfcf; }
  .brand-section { position: absolute; left: 286px; top: 31px; font-family: "Yanone Kaffeesatz", sans-serif; font-weight: 300; font-size: 23px; color: #8a8a8a; }

  .main-nav { position: absolute; top: 29px; left: 0; width: 1200px; }
  .main-nav a { position: absolute; font-family: "Yanone Kaffeesatz", sans-serif; font-weight: 700; font-size: 26px; line-height: 1; color: var(--ink); text-decoration: none; letter-spacing: 0.3px; }

  .hero { position: absolute; left: 0; top: 90px; width: 1200px; height: 455px;
    background: radial-gradient(ellipse at 52% 20%, #9cc7da 0%, #73a6bd 35%, #4f8397 70%, #3e6d80 100%); }
  .hero-arrow { position: absolute; top: 206px; width: 51px; height: 52px; background: var(--arrow-bg); display: flex; align-items: center; justify-content: center; }
  .hero-arrow.prev { left: 0; border-radius: 0 4px 4px 0; }
  .hero-arrow.next { right: 0; border-radius: 4px 0 0 4px; }

  .hero-gap { position: absolute; left: 0; top: 545px; width: 1200px; height: 3px; background: #fff; }

  .promo { position: absolute; left: 0; top: 548px; width: 1200px; height: 114px; background: var(--orange); }
  .promo-text { position: absolute; left: 161px; top: 24px; width: 580px; font-weight: 300; font-size: 16.7px; line-height: 21px; color: #fff; }
  .btn-light { position: absolute; left: 845px; top: 37px; width: 156px; height: 38px; border-radius: 3px;
    background: linear-gradient(#ffffff, #ececec); color: #333; font-weight: 700; font-size: 12px; letter-spacing: 0.4px;
    display: flex; align-items: center; justify-content: center; text-decoration: none; }

  .culture { position: absolute; top: 690px; width: 392px; }
  .culture.left { left: 163px; }
  .culture.right { left: 657px; }
  .culture h2 { font-family: "Bree Serif", serif; font-weight: 400; font-size: 26px; line-height: 1; color: var(--orange-deep); padding-bottom: 11px; border-bottom: 1px solid var(--rule); }
  .culture h3 { margin-top: 12px; font-family: "Yanone Kaffeesatz", sans-serif; font-weight: 300; font-size: 21px; line-height: 1; color: #3f3f3f; letter-spacing: 0.4px; }
  .values { list-style: none; margin-top: 18px; }
  .values li { display: flex; align-items: center; font-weight: 300; font-size: 13.3px; color: #444; height: 16px; }
  .values li + li { margin-top: 10px; }
  .values li:last-child { margin-top: 13px; }
  .values .num { width: 16px; height: 16px; border-radius: 50%; background: var(--orange-deep); color: #fff; font-size: 9px; font-weight: 700; display: flex; align-items: center; justify-content: center; margin-right: 12px; flex: none; }
  .btn-dark { display: flex; margin-top: 25px; margin-left: 1px; width: 156px; height: 38px; border-radius: 3px;
    background: linear-gradient(#3a4247, #1a1f22); color: #fff; font-weight: 700; font-size: 12px; letter-spacing: 0.2px;
    align-items: center; justify-content: center; text-decoration: none; }

  .site-footer { position: absolute; left: 0; top: 959px; width: 1200px; height: 62px; background: var(--footer); }
  .footer-nav { position: absolute; left: 164px; top: 26px; display: flex; gap: 13px; }
  .footer-nav a, .copyright { font-size: 11.5px; color: var(--footer-text); text-decoration: none; }
  .copyright { position: absolute; right: 151px; top: 26px; }
</style>
</head>
<body>
  <div class="top-strip"></div>

  <header class="site-header">
    <div class="brand">
      <div class="brand-name">Brantley</div>
      <div class="brand-tag">AGENCE NUMÉRIQUE</div>
    </div>
    <div class="brand-divider"></div>
    <div class="brand-section">Careers</div>
    <nav class="main-nav">
      <a href="#" style="left:626px">BMANIFESTE</a>
      <a href="#" style="left:751px">OPPORTUNITÉS</a>
      <a href="#" style="left:897px">BRANTLY</a>
      <a href="#" style="left:994px">POSTULER</a>
    </nav>
  </header>

  <section class="hero" role="img" aria-label="Photo of a smiling woman writing notes on a glass board against a blue backdrop">
    <a class="hero-arrow prev" href="#" aria-label="Previous slide">
      <svg width="14" height="24" viewBox="0 0 14 24"><path d="M11 3 L3 12 L11 21" fill="none" stroke="#d9e9f1" stroke-width="3.5" stroke-linecap="round" stroke-linejoin="round"/></svg>
    </a>
    <a class="hero-arrow next" href="#" aria-label="Next slide">
      <svg width="14" height="24" viewBox="0 0 14 24"><path d="M3 3 L11 12 L3 21" fill="none" stroke="#d9e9f1" stroke-width="3.5" stroke-linecap="round" stroke-linejoin="round"/></svg>
    </a>
  </section>
  <div class="hero-gap"></div>

  <section class="promo">
    <p class="promo-text">Lorem ipsum dolor sit amet, consectetuer adipiscing elit. Aenean commodo ligula eget dolor. Aenean massa. Cum sociis natoque penatibus et magnis dis parturient montes,</p>
    <a class="btn-light" href="#">LEARN MORE</a>
  </section>

  <section class="culture left">
    <h2>The agency’s corporate culture :</h2>
    <h3>Do you embrace Brantley's corporate culture?</h3>
    <ol class="values">
      <li><span class="num">1</span>Lorem Ipsum is simply dummy text of the printing and typeset</li>
      <li><span class="num">2</span>Lorem Ipsum is simply dummy text of the printing and</li>
      <li><span class="num">3</span>Lorem Ipsum is simply dummy text of the printing and</li>
    </ol>
    <a class="btn-dark" href="#">APPLY NOW</a>
  </section>

  <section class="culture right">
    <h2>The agency’s corporate culture :</h2>
    <h3>Do you embrace Brantley's corporate culture?</h3>
    <ol class="values">
      <li><span class="num">1</span>Lorem Ipsum is simply dummy text of the printing and typeset</li>
      <li><span class="num">2</span>Lorem Ipsum is simply dummy text of the printing and</li>
      <li><span class="num">3</span>Lorem Ipsum is simply dummy text of the printing and</li>
    </ol>
    <a class="btn-dark" href="#">APPLY NOW</a>
  </section>

  <footer class="site-footer">
    <nav class="footer-nav">
      <a href="#">bManifeste</a>
      <a href="#">Opportunités</a>
      <a href="#">Brantly</a>
      <a href="#">Postuler</a>
    </nav>
    <p class="copyright">(c) 2012 Brantley,&nbsp; All rights reserved</p>
  </footer>
</body>
</html>
```